Velmo und Korvex Smartphone Reparatur - PPC - Affiliate
Zielgruppe
Wir gründen ein Unternehmen, welches sich ausschließlich mit hochwertigen Reparaturen von Velmos und Korvex Smartphones beschäftigt. Wir bieten Reparaturen innerhalb 48 Stunden, hochwertige Ersatzteile und die Abholung des Gerätes von zu Hause an. Einen Slogan haben wir noch nicht.
Aufgabenstellung
Da wir ein Unternehmen im Bereich Technologie gründen, ist es wichtig für uns, dass man "Technik" sieht. Die Banner sollten deshalb auf jedenfall modern sein und möglichst das Orange/Weiß oder Orange/Schwarz der Startseite unserer Website beinhalten.
Die größen der Banner:
250 x 250
200 x 200
468 x 60
728 x 90
300 x 250
120 x 600
160 x 600
Einen Slogan haben wir noch nicht.
Sollten Sie für die Banner etwas von unserer Website benötigen, dürfen Sie sich gerne bedienen.
www.lunqor.de

```html
<!DOCTYPE html>
<html lang="de">
<head>
<meta charset="utf-8">
<title>Lunqor Smartphone Reparatur – Banner 300×250</title>
<link rel="stylesheet" href="https://fonts.googleapis.com/css2?family=PT+Sans:wght@400;700&display=swap">
<style>
  :root {
    --orange: #f7a133;
    --orange-deep: #f08c1c;
    --white: #ffffff;
    --ink: #1d1d1d;
    --glass-dark: #121212;
    --glass-mid: #3a3a3a;
    --photo-light: #d9dcd6;
    --photo-mid: #8f9a8c;
    --stage: #eeeeee;
  }
  * { box-sizing: border-box; margin: 0; padding: 0; }
  html, body {
    width: 1041px; height: 1200px; overflow: hidden;
    background: var(--stage);
    font-family: "PT Sans", Arial, sans-serif;
  }
  .banner-frame {
    position: absolute; left: 40px; top: 200px;
    width: 960px; height: 800px;
  }
  .banner {
    position: absolute; left: 0; top: 0;
    width: 300px; height: 250px;
    transform: scale(3.2); transform-origin: 0 0;
    overflow: hidden;
    background: linear-gradient(135deg, var(--glass-mid) 0%, var(--glass-dark) 45%, #262626 75%, var(--glass-mid) 100%);
  }
  .header {
    position: absolute; left: 0; top: 0; width: 300px; height: 38px;
    background: var(--orange);
  }
  .brand {
    position: absolute; left: 8px; top: 8px;
    display: flex; align-items: center; gap: 6px;
    color: var(--white);
  }
  .brand-dot {
    width: 22px; height: 22px; border-radius: 50%;
    background: var(--white);
  }
  .brand-name {
    font-weight: 700; font-size: 19px; letter-spacing: 1px; line-height: 1;
  }
  .brand-tag {
    font-weight: 700; font-size: 6.5px; line-height: 1.05; margin-top: 4px;
  }
  .phone-box {
    position: absolute; left: 185px; top: 11px; width: 110px; height: 23px;
    border: 1.2px solid var(--white); border-radius: 2px;
    color: var(--white); font-weight: 700; font-size: 13px;
    display: flex; align-items: center; justify-content: center;
  }
  .glass-photo {
    position: absolute; left: 0; top: 38px; width: 300px; height: 212px;
    background: radial-gradient(ellipse at 80% 40%, rgba(255,255,255,0.12), transparent 60%);
  }
  .repair-photo {
    position: absolute; left: -40px; top: 45px; width: 200px; height: 200px;
    border-radius: 50%;
    background: radial-gradient(circle at 55% 55%, #2b2f2c 0%, var(--photo-mid) 45%, var(--photo-light) 80%);
  }
  .url-plate {
    position: absolute; left: 0; top: 222px; width: 150px; height: 28px;
    background: linear-gradient(90deg, #f3f3f1, #e4e5e1);
  }
  .url {
    position: absolute; left: 22px; top: 227px;
    font-weight: 700; font-size: 15.5px; color: var(--ink);
  }
  .feature {
    position: absolute; display: flex; align-items: center; gap: 8px;
  }
  .feature-icon {
    width: 30px; height: 30px; border-radius: 50%;
    background: var(--white);
    display: flex; align-items: center; justify-content: center;
    flex-shrink: 0;
  }
  .feature-text {
    color: var(--white); font-weight: 700; font-size: 10px; line-height: 1.15;
  }
  .f-parts   { left: 121px; top: 52px; }
  .f-pro     { left: 151px; top: 92px; }
  .f-fast    { left: 163px; top: 134px; }
  .f-ship    { left: 155px; top: 177px; }
  .cta {
    position: absolute; left: 153px; top: 218px; width: 142px; height: 27px;
    background: var(--orange); border-radius: 3px;
    color: var(--white); font-weight: 700; font-size: 16px;
    display: flex; align-items: center; justify-content: center;
  }
</style>
</head>
<body>
  <div class="banner-frame">
    <div class="banner">
      <div class="glass-photo" role="img" aria-label="Hintergrundfoto: zersplittertes Display-Glas in Schwarz und Grau"></div>
      <div class="repair-photo" role="img" aria-label="Foto: geöffnetes Smartphone mit Akku bei der Reparatur mit Werkzeug"></div>

      <header class="header">
        <div class="brand">
          <span class="brand-dot"></span>
          <span class="brand-name">LUNQOR</span>
          <span class="brand-tag">Smartphone<br>Reparatur</span>
        </div>
        <div class="phone-box">+321 555 0147</div>
      </header>

      <div class="feature f-parts">
        <span class="feature-icon">
          <svg width="14" height="18" viewBox="0 0 14 18"><rect x="1.5" y="1" width="11" height="16" rx="2" fill="none" stroke="#f7a133" stroke-width="2"/><circle cx="7" cy="14" r="1" fill="#f7a133"/></svg>
        </span>
        <span class="feature-text">Hochwertige<br>Ersatzteile</span>
      </div>

      <div class="feature f-pro">
        <span class="feature-icon">
          <svg width="16" height="16" viewBox="0 0 16 16"><circle cx="8" cy="5" r="3.6" fill="#f7a133"/><path d="M1 16c0-4 3-6.5 7-6.5s7 2.5 7 6.5z" fill="#f7a133"/></svg>
        </span>
        <span class="feature-text">Professionelle<br>Reparatur</span>
      </div>

      <div class="feature f-fast">
        <span class="feature-icon">
          <svg width="18" height="18" viewBox="0 0 18 18"><circle cx="9" cy="9" r="7.5" fill="none" stroke="#f7a133" stroke-width="2"/><path d="M9 4.5V9l3 2" fill="none" stroke="#f7a133" stroke-width="2" stroke-linecap="round"/></svg>
        </span>
        <span class="feature-text">Reparatur<br>innerhalb 48H</span>
      </div>

      <div class="feature f-ship">
        <span class="feature-icon">
          <svg width="18" height="18" viewBox="0 0 18 18"><path d="M16.5 1.5c-1-1-2.5 0-3.5 1l-3 3-7-2-1.5 1.5 5.5 3.5-3 3-2.5-.5-1 1 3 1.5 1.5 3 1-1-.5-2.5 3-3 3.5 5.5 1.5-1.5-2-7 3-3c1-1 2-2.5 1-3.5z" fill="#f7a133"/></svg>
        </span>
        <span class="feature-text">Bequemer<br>Versand</span>
      </div>

      <div class="url-plate"></div>
      <div class="url">www.lunqor.de</div>
      <div class="cta">KLICKEN HIER</div>
    </div>
  </div>
</body>
</html>
```